Truck Sign Writing Design

Looking for some help with designing the sign writing to go on our small truck. We have our company logos already. Our truck is fitted with black acm panels on the sides ready to go. The trucks cab is currently getting repainted white - the black side panels will remain with black showing and the sign writing will be put over the top - Black will remain being the background colour) (Please incorporate this into your design)
. Would like to get designs on the front of the truck, both doors, and each side panels. The services we provide are Tree Removal, Tree Pruning, and Stump Grinding, which may be incorporated into the design.
Ideally we would like our logo, our services (as above), phone number 027391604 and possibly website (www.brindlewoodarbor.co.nz) on the truck. This may or may not be needed in all areas. etc front of truck. Open to ideas and Suggestions.
Design must include Illustrator .AI file.
Company colours black and green (#5b842b)
Attached is our truck and example of the front (another truck).
Font used is - Trajan Pro Bold

```html
<!DOCTYPE html>
<html lang="en">
<head>
<meta charset="utf-8">
<title>Brindlewood Arbor Solutions – Transport Signage</title>
<link rel="stylesheet" href="https://fonts.googleapis.com/css2?family=Cinzel:wght@400;600;700&display=swap">
<style>
  :root {
    --board-green: #4aa300;
    --accent-green: #55b01c;
    --panel-black: #000000;
    --panel-glow: #0f2a10;
    --text-white: #ffffff;
  }
  * { margin: 0; padding: 0; box-sizing: border-box; }
  html, body { width: 1200px; height: 849px; overflow: hidden; }
  body {
    background: var(--board-green);
    font-family: "Cinzel", "Trajan Pro", serif;
    color: var(--text-white);
    position: relative;
  }
  .board-title {
    position: absolute; top: 52px; left: 0; width: 1200px;
    text-align: center; font-size: 18px; font-weight: 600;
    letter-spacing: 7px;
  }
  .sign-panel {
    position: absolute; top: 220px; width: 520px; height: 390px;
    background: radial-gradient(ellipse at 70% 75%, var(--panel-glow) 0%, var(--panel-black) 60%);
    box-shadow: 6px 8px 14px rgba(0,0,0,.35);
    display: flex; flex-direction: column; align-items: center;
  }
  .sign-panel--brand { left: 45px; }
  .sign-panel--services { left: 635px; }

  .company-name {
    color: var(--text-white); font-weight: 700; line-height: 1.1;
    text-align: center; letter-spacing: 2px;
  }
  .call-badge {
    background: var(--accent-green); color: var(--text-white);
    font-weight: 700; line-height: 1; letter-spacing: 1px;
  }
  .phone-number { font-weight: 400; line-height: 1; color: var(--text-white); white-space: nowrap; }
  .website { font-weight: 600; letter-spacing: .5px; }

  /* brand panel */
  .sign-panel--brand .company-name { font-size: 30px; margin-top: 92px; }
  .sign-panel--brand .call-badge { font-size: 15px; padding: 3px 10px; margin-top: 34px; }
  .sign-panel--brand .phone-number { font-size: 66px; margin-top: 8px; }
  .sign-panel--brand .website { font-size: 11px; margin-top: 26px; }

  /* services panel */
  .services-heading { color: var(--accent-green); font-size: 21px; font-weight: 600; margin-top: 38px; }
  .services-list { font-size: 20px; font-weight: 700; text-align: center; line-height: 1.35; margin-top: 14px; letter-spacing: .5px; }
  .sign-panel--services .call-badge { font-size: 15px; padding: 3px 10px; margin-top: 20px; }
  .sign-panel--services .phone-number { font-size: 64px; margin-top: 6px; }
  .sign-panel--services .company-name { font-size: 15px; margin-top: 34px; }
  .sign-panel--services .website { font-size: 11px; margin-top: 18px; }
</style>
</head>
<body>
  <h1 class="board-title">BRINDLEWOOD – ARBOR SOLUTIONS TRANSPORT SIGNAGES</h1>

  <section class="sign-panel sign-panel--brand">
    <p class="company-name">BRINDLEWOOD<br>ARBOR SOLUTIONS</p>
    <p class="call-badge">CALL</p>
    <p class="phone-number">027-391-604</p>
    <p class="website">WWW.BRINDLEWOODARBOR.CO.NZ</p>
  </section>

  <section class="sign-panel sign-panel--services">
    <h2 class="services-heading">OUR SERVICES</h2>
    <p class="services-list">TREE REMOVAL • TREE PRUNING<br>STUMP GRINDING</p>
    <p class="call-badge">CALL</p>
    <p class="phone-number">027-391-604</p>
    <p class="company-name">BRINDLEWOOD ARBOR SOLUTIONS</p>
    <p class="website">WWW.BRINDLEWOODARBOR.CO.NZ</p>
  </section>
</body>
</html>
```